Corvant Systems Business Card

Create an appealing and elegant Business card for corvant systems. Include logo and use related colors from website, be creative. Include Business name, my name, tile, address, contacts, address, and social media contacts if possible. Logo PSD file is attached.

Bleed Area: 3.46" x 2.32"
Trim: 3.3" x 2.16"
Safe Area: 3.14" x 2.02"

Save files as vector-based PDF with outlined text and PNG.
No crop marks
CMYK color setting

Business Card Info:

Corvant Systems

Dennis Halvorsen
Owner

512 Brindlemoor Rd Unit C
Harlow Mills, VT 02871
t. 1.888.555.0162
e. dennis.h@corvantsys.example
w. www.corvantsys.example

facebook. www.facebook.com/CorvantSys
twitter. twitter.com/corvantsys
pinterest. www.pinterest.com/corvantsys/

Target Market(s)

Business Owners and Partners

Industry/Entity Type

Business

Requirements
Must have
• Logo and related colors from website

```html
<!DOCTYPE html>
<html lang="en">
<head>
<meta charset="utf-8">
<title>Corvant Systems Business Card</title>
<link rel="stylesheet" href="https://fonts.googleapis.com/css2?family=Arvo:wght@400;700&family=Open+Sans:wght@400&display=swap">
<style>
  :root {
    --page: #e9e6e1;
    --card-white: #ffffff;
    --card-black: #0b0b0b;
    --band-black: #050505;
    --brand-blue: #1b8fe3;
    --ink: #1c1c1c;
    --ink-soft: #3a3a3a;
    --social-one: #1877e8;
    --social-two: #1da1f2;
    --social-three: #e0484c;
    --shadow: rgba(0,0,0,.18);
  }
  * { box-sizing: border-box; margin: 0; padding: 0; }
  html, body { width: 1200px; height: 900px; overflow: hidden; }
  body {
    background: var(--page);
    font-family: "Arvo", Georgia, serif;
    position: relative;
  }
  .card {
    position: absolute;
    left: 300px;
    width: 600px;
    height: 343px;
    box-shadow: 0 6px 18px var(--shadow);
    overflow: hidden;
  }
  .card--front { top: 88px; background: var(--card-black); }
  .card--back { top: 471px; background: var(--card-white); }

  .wordmark {
    font-family: "Open Sans", Arial, sans-serif;
    font-weight: 400;
    line-height: 1;
    letter-spacing: .5px;
  }
  .wordmark span { display: block; }
  .card--front .wordmark {
    position: absolute;
    left: 0; right: 0; top: 128px;
    text-align: center;
    color: #ffffff;
    font-size: 44px;
  }

  .holder {
    position: absolute;
    left: 0; width: 600px; top: 26px;
    text-align: center;
  }
  .holder__name {
    color: var(--brand-blue);
    font-weight: 700;
    font-size: 21px;
    letter-spacing: 1px;
    text-transform: uppercase;
  }
  .holder__title {
    color: var(--ink);
    font-weight: 700;
    font-size: 14px;
    margin-top: 2px;
  }

  .contact-band {
    position: absolute;
    left: 0; top: 96px;
    width: 380px; height: 140px;
    background: var(--band-black);
  }
  .contact-list {
    position: absolute;
    right: 74px; top: 10px;
    list-style: none;
    text-align: right;
    color: var(--brand-blue);
    font-size: 15px;
    line-height: 1.15;
  }
  .contact-list li { margin-bottom: 9px; white-space: nowrap; }
  .contact-icons {
    position: absolute;
    right: 0; top: 0;
    width: 70px; height: 140px;
  }

  .card--back .wordmark {
    position: absolute;
    left: 400px; top: 130px;
    color: var(--ink);
    font-size: 33px;
  }

  .socials {
    position: absolute;
    left: 0; right: 0; bottom: 24px;
    display: flex;
    justify-content: space-around;
    padding: 0 30px;
  }
  .social {
    display: flex;
    flex-direction: column;
    align-items: center;
    gap: 6px;
    color: var(--ink-soft);
    font-weight: 700;
    font-size: 17px;
  }
  .social__dot { width: 26px; height: 26px; border-radius: 50%; }
  .social--one .social__dot { background: var(--social-one); }
  .social--two .social__dot { background: var(--social-two); }
  .social--three .social__dot { background: var(--social-three); }
</style>
</head>
<body>

  <section class="card card--front" aria-label="Card front">
    <div class="wordmark"><span>Corvant</span><span>Systems</span></div>
  </section>

  <section class="card card--back" aria-label="Card back">
    <header class="holder">
      <p class="holder__name">Dennis Halvorsen</p>
      <p class="holder__title">Owner</p>
    </header>

    <div class="contact-band">
      <ul class="contact-list">
        <li>1.888.555.0162</li>
        <li>dennis.h@corvantsys.example</li>
        <li>www.corvantsys.example</li>
        <li>512 Brindlemoor Rd Unit C<br>Harlow Mills, VT 02871</li>
      </ul>
      <svg class="contact-icons" viewBox="0 0 70 140" aria-hidden="true">
        <g fill="var(--brand-blue)">
          <rect x="22" y="15" width="48" height="8"/>
          <rect x="22" y="43" width="48" height="8"/>
          <rect x="22" y="71" width="48" height="8"/>
          <rect x="22" y="99" width="48" height="8"/>
        </g>
        <g fill="#ffffff" stroke="var(--brand-blue)" stroke-width="2">
          <circle cx="22" cy="19" r="11"/>
          <circle cx="22" cy="47" r="11"/>
          <circle cx="22" cy="75" r="11"/>
          <circle cx="22" cy="103" r="11"/>
        </g>
        <path d="M16 17 q6 -5 12 0 l-1.5 2 h-2 l-.5-1.5 h-4 l-.5 1.5 h-2z M17.5 20 h9 v3 h-9z" fill="#111"/>
        <rect x="15.5" y="42.5" width="13" height="9" fill="#111"/>
        <path d="M15.5 42.5 L22 48 L28.5 42.5" fill="none" stroke="#fff" stroke-width="1.2"/>
        <g fill="none" stroke="#111" stroke-width="1.2">
          <circle cx="22" cy="75" r="6.5"/>
          <ellipse cx="22" cy="75" rx="3" ry="6.5"/>
          <line x1="15.5" y1="75" x2="28.5" y2="75"/>
        </g>
        <path d="M15 103.5 L22 97 L29 103.5 H27 V109 H23.5 V105.5 H20.5 V109 H17 V103.5z" fill="#111"/>
      </svg>
    </div>

    <div class="wordmark"><span>Corvant</span><span>Systems</span></div>

    <div class="socials">
      <div class="social social--one"><span class="social__dot"></span>CorvantSys</div>
      <div class="social social--two"><span class="social__dot"></span>corvantsys</div>
      <div class="social social--three"><span class="social__dot"></span>corvantsys</div>
    </div>
  </section>

</body>
</html>
```